Business Card Design Project

I have just chosen a logo and would now like this designed onto a business card for my hair salon. I would like it to be classy not to busy and have a wow factor when people look at them
Has to Include on card:
Logo Design
And business details below
Kaycee-rae Whitlow (owner)
0481 726 304
Lmv@brindal.com.au
57 Corella Street Kinross Vale
Logo is now attached please provide designs
Hair

```html
<!DOCTYPE html>
<html lang="en">
<head>
<meta charset="utf-8">
<title>Lumen Hair Atelier – Business Card</title>
<link rel="stylesheet" href="https://fonts.googleapis.com/css2?family=Open+Sans:wght@700&family=Jost:wght@400;500&display=swap">
<style>
  :root {
    --backdrop: #d6d6d6;
    --card: #ffffff;
    --ink: #1a1a1a;
    --magenta: #c4166f;
    --magenta-deep: #8e1c5e;
    --teal: #3fb6c4;
    --ghost: #efefef;
  }
  * { margin: 0; padding: 0; box-sizing: border-box; }
  html, body {
    width: 1200px;
    height: 800px;
    overflow: hidden;
    background: var(--backdrop);
  }
  .canvas {
    position: relative;
    width: 1200px;
    height: 800px;
  }
  .business-card {
    position: absolute;
    left: 150px;
    top: 140px;
    width: 900px;
    height: 520px;
    background: var(--card);
    overflow: hidden;
    box-shadow: 0 6px 18px rgba(0, 0, 0, 0.18);
  }
  .ghost-mark {
    position: absolute;
    right: -40px;
    top: 90px;
    width: 400px;
    height: 400px;
    border-radius: 50%;
    background: var(--ghost);
  }
  .brand {
    position: absolute;
    left: 60px;
    top: 120px;
    display: flex;
    align-items: center;
    gap: 34px;
  }
  .brand-dot {
    width: 190px;
    height: 190px;
    border-radius: 50%;
    background: linear-gradient(160deg, var(--magenta), var(--magenta-deep));
    flex: none;
  }
  .brand-name {
    font-family: "Jost", sans-serif;
    font-weight: 500;
    font-size: 58px;
    line-height: 1.05;
    letter-spacing: 3px;
    text-transform: uppercase;
    color: var(--magenta);
  }
  .owner-name {
    position: absolute;
    right: 52px;
    top: 42px;
    font-family: "Open Sans", sans-serif;
    font-weight: 700;
    font-size: 28px;
    color: var(--ink);
  }
  .contact {
    position: absolute;
    right: 52px;
    bottom: 44px;
    text-align: right;
    font-family: "Jost", sans-serif;
    font-weight: 400;
    font-size: 23px;
    line-height: 1.45;
    color: var(--ink);
    font-style: normal;
  }
</style>
</head>
<body>
  <main class="canvas">
    <section class="business-card">
      <div class="ghost-mark" aria-hidden="true"></div>

      <div class="brand">
        <div class="brand-dot" aria-hidden="true"></div>
        <p class="brand-name">Lumen<br>Hair Atelier</p>
      </div>

      <h1 class="owner-name">Kaycee-rae Whitlow</h1>

      <address class="contact">
        57 Corella Street Kinross Vale<br>
        Lmv@brindal.com.au<br>
        0481 726 304
      </address>
    </section>
  </main>
</body>
</html>
```